Need A Modern Website Design For ADSL2+ Provider

AIM: To sell affordable combined ADSL2+ Unlimited & phone line rentals to residential customers.

TYPE: This project is for DESIGN only (no code)

Source Files: I need all source files, fonts, images to be provided in ZIP format.

Logo: Existing (attached)

-Corporate Colours-
Black & Red (Same as Logo)
Others colours are fine as long as it looks corporate and modern.

-Pages-
Need another page to display our pricing plan

(1)Homepage Design
(2)Page to display our plans (needs to be in tables)
Example: http://lnkshrt.example/Qv7Rp2

-Pricing Plan-
(1) $59.95 / Month (Metro / City Areas)
(2) $79.95 / Month (Outside City Areas / Rural Areas)
Detailed Pricing plans is in PDF attached
Updates

Just letting everyone know we have picked a designer, thank you for all you submissions.

Target Market(s)

Both male & female, Young & Old

Industry/Entity Type

Residential

Requirements
Must have
• + Graphic banner on the home page that shows our ADSL2+ combo plan for ADSL2+ Unlimited & Phone Line Rental for only $59.95

+ A box to allow customers to login to their account (username & password + login button)

+ Clearly display contact number
+ Button to sign up
+ Button to check service availability something like https://linkup.vexora.com/wizard/

+ Button for Live Chat
+ Navigation menu
+ Social media icons Chatterly, Plexo +, Chirpnet
+ Minimal text on homepage
+ Corporate & Friendly
Nice to have
• + Effective use of icons with corporate colours
+ Effective use of stockphotos
(use of people in photos would be nice)

+ Effective use of graphics to navigate people through the site and inform customers of specials,etc.
Should not have
• + Cluttered
+ Don’t want long scrolling homepage
+ Don’t want too much text on homepage 500 words is the estimate max.

```html
<!DOCTYPE html>
<html lang="en">
<head>
<meta charset="utf-8">
<title>Veltrix — ADSL2+ &amp; Phone Line</title>
<link rel="stylesheet" href="https://fonts.googleapis.com/css2?family=Open+Sans:wght@400;600;700&family=Roboto+Condensed:wght@300;400&family=Archivo+Black&display=swap">
<style>
:root{
  --ink:#111;
  --black:#0a0a0a;
  --white:#fff;
  --red:#d91a12;
  --grey-panel:#eceef2;
  --grey-line:#c9c9c9;
  --grey-text:#555;
  --green:#5fb12f;
}
*{box-sizing:border-box;margin:0;padding:0}
html,body{width:1100px;height:1200px;overflow:hidden;background:var(--white);font-family:"Open Sans",Arial,sans-serif;color:var(--ink)}
.page{position:relative;width:1100px;height:1200px}

/* header */
.brand{position:absolute;left:33px;top:50px;display:flex;align-items:center;gap:14px}
.brand-dot{width:62px;height:62px;border-radius:50%;background:var(--black)}
.brand-name{font-size:46px;font-weight:600;letter-spacing:2px;color:var(--black)}
.hotline{position:absolute;right:20px;top:38px;display:flex;align-items:center;gap:14px;font-size:23px;letter-spacing:1.5px}
.search{position:absolute;left:724px;top:89px;width:252px;height:33px;border:1px solid var(--grey-line);border-radius:4px;display:flex;align-items:center;padding-left:10px;font-size:15px;color:#777}
.search svg{position:absolute;right:8px;top:6px}
.search::after{content:"";position:absolute;right:40px;top:5px;bottom:5px;border-left:1px dotted #aaa}
.btn-signup{position:absolute;left:987px;top:89px;width:93px;height:33px;background:var(--black);color:var(--white);border-radius:4px;font-size:17px;display:flex;align-items:center;justify-content:center}

/* nav */
.main-nav{position:absolute;left:0;top:158px;width:1100px;height:44px;background:linear-gradient(#3a3a3a,#000 40%,#111);display:flex}
.main-nav a{color:var(--white);text-decoration:none;font-size:15px;font-weight:700;letter-spacing:.5px;display:flex;align-items:center;justify-content:center;border-right:1px solid #666;height:100%}

/* hero */
.hero{position:absolute;left:19px;top:223px;width:1062px;height:339px;border:2px solid #222;background:linear-gradient(90deg,#eeeff3 0%,#f2f3f6 55%,#e4e6ea 100%);overflow:hidden}
.hero-text{position:absolute;left:38px;top:68px;font-family:"Roboto Condensed",Arial,sans-serif;color:#111;text-transform:uppercase}
.hero-text .l1{font-size:34px;font-weight:300;display:block}
.hero-text .l2{font-size:44px;font-weight:400;display:block;margin-top:18px}
.hero-text .l3{font-size:34px;font-weight:300;display:block;margin-top:18px}
.hero-photo{position:absolute;right:0;top:0;width:470px;height:100%;background:linear-gradient(90deg,rgba(238,239,243,0),#d9d4cf 35%,#3c2a22 60%,#1c2a4a 90%)}

/* plan cards */
.plan{position:absolute;top:582px;height:306px;background:linear-gradient(#2a2a2a,#050505 40%,#000);color:var(--white)}
.plan-metro{left:18px;width:505px}
.plan-rural{left:563px;width:520px}
.plan h2{position:absolute;left:22px;top:22px;font-size:22px;font-weight:400;letter-spacing:1.5px}
.plan-phone{position:absolute;left:24px;top:95px;width:150px;height:190px;border-radius:20px;background:linear-gradient(#8a8a8a,#444 60%,#222)}
.plan-bubble{position:absolute;left:182px;top:62px}
.price{font-family:"Archivo Black",Arial,sans-serif;font-size:33px;fill:var(--white)}
.read-more{position:absolute;bottom:22px;right:22px;width:135px;height:33px;background:linear-gradient(#fff,#ddd);color:#111;border-radius:3px;font-size:14px;font-weight:700;display:flex;align-items:center;justify-content:center}
.divider{position:absolute;left:543px;top:592px;width:1px;height:286px;background:#ddd}

/* availability */
.availability{position:absolute;left:19px;top:907px;width:1062px;height:130px;background:var(--grey-panel)}
.availability h3{position:absolute;left:21px;top:12px;font-size:29px;font-weight:400;line-height:33px;letter-spacing:1px;color:#222}
.phone-field{position:absolute;left:226px;top:28px;width:516px;height:73px;display:flex}
.phone-field .icon{width:82px;height:80px;background:var(--black);border-radius:8px;margin-top:-3px;display:flex;align-items:center;justify-content:center;position:relative;z-index:1}
.phone-field .input{flex:1;margin-left:-4px;border:3px solid #000;background:var(--white);border-radius:0 4px 4px 0;font-size:22px;color:#999;display:flex;align-items:center;padding-left:14px;letter-spacing:.5px}
.btn-view{position:absolute;left:760px;top:28px;width:177px;height:73px;background:var(--black);border-radius:4px;color:var(--white);font-size:22px;display:flex;align-items:center;justify-content:center;gap:10px}

/* footer */
.footer-rule{position:absolute;left:0;top:1068px;width:1100px;border-top:1px solid #bbb}
.footer-links{position:absolute;left:16px;top:1096px;font-size:14px;letter-spacing:.5px;color:#111}
.footer-bar{position:absolute;left:0;top:1144px;width:1100px;height:56px;background:var(--black);color:var(--white)}
.copyright{position:absolute;left:16px;top:18px;font-size:13.5px}
.social{position:absolute;right:16px;top:12px;display:flex;gap:12px}
.social span{width:34px;height:32px;border-radius:4px;background:linear-gradient(#f4f4f4,#bdbdbd)}
</style>
</head>
<body>
<div class="page">
  <header>
    <div class="brand"><span class="brand-dot"></span><span class="brand-name">VELTRIX</span></div>
    <div class="hotline">
      <svg width="34" height="34" viewBox="0 0 34 34" aria-hidden="true"><circle cx="17" cy="17" r="16" fill="var(--green)"/><path d="M9 13c0-3 16-3 16 0v2h-4v-2h-8v2H9z M11 17h12l2 8H9z" fill="#fff"/></svg>
      <span>+91 90 555 014</span>
    </div>
    <div class="search">Search...
      <svg width="22" height="22" viewBox="0 0 22 22" aria-hidden="true"><circle cx="9" cy="9" r="6.5" fill="none" stroke="#111" stroke-width="2.5"/><path d="M14 14l6 6" stroke="#111" stroke-width="3"/></svg>
    </div>
    <div class="btn-signup">SIGN UP</div>
  </header>

  <nav class="main-nav">
    <a style="width:145px">Home</a><a style="width:188px">Plans</a><a style="width:199px">Equipment</a><a style="width:209px">Call Rates</a><a style="width:194px">Support</a><a style="width:165px;border-right:0">Contact Us</a>
  </nav>

  <section class="hero">
    <div class="hero-photo" role="img" aria-label="Photo of a smiling woman looking at her mobile phone"></div>
    <p class="hero-text"><span class="l1">Affordable combined</span><span class="l2">ADSL2+ Unlimited &amp; Phone Line</span><span class="l3">Rentals to residential customers.</span></p>
  </section>

  <article class="plan plan-metro">
    <h2>FOR METRO / CITY AREAS</h2>
    <div class="plan-phone" role="img" aria-label="Grey cordless home phone on its base"></div>
    <svg class="plan-bubble" width="240" height="180" viewBox="0 0 240 180" aria-hidden="true">
      <path d="M120 2C55 2 2 35 2 78c0 40 45 72 105 76l-22 24 50-26c60-6 103-37 103-74C238 35 185 2 120 2z" fill="var(--red)" stroke="#fff" stroke-width="3"/>
      <text class="price" x="120" y="50" text-anchor="middle">$59.95</text>
      <text class="price" x="120" y="84" text-anchor="middle">Per</text>
      <text class="price" x="120" y="118" text-anchor="middle">Month</text>
    </svg>
    <div class="read-more">Read More..</div>
  </article>
  <div class="divider"></div>
  <article class="plan plan-rural">
    <h2>OUTSIDE CITY AREAS / RURAL AREAS</h2>
    <div class="plan-phone" role="img" aria-label="Silver cordless phone with blue display on its base" style="background:linear-gradient(#cfcfcf,#8d8d8d 50%,#e5e5e5)"></div>
    <svg class="plan-bubble" width="240" height="180" viewBox="0 0 240 180" aria-hidden="true">
      <path d="M120 2C55 2 2 35 2 78c0 40 45 72 105 76l-22 24 50-26c60-6 103-37 103-74C238 35 185 2 120 2z" fill="var(--red)" stroke="#fff" stroke-width="3"/>
      <text class="price" x="120" y="50" text-anchor="middle">$79.95</text>
      <text class="price" x="120" y="84" text-anchor="middle">Per</text>
      <text class="price" x="120" y="118" text-anchor="middle">Month</text>
    </svg>
    <div class="read-more">Read More..</div>
  </article>

  <section class="availability">
    <h3>Check<br>Service<br>Availability</h3>
    <div class="phone-field">
      <div class="icon"><svg width="44" height="52" viewBox="0 0 44 52" aria-hidden="true"><path d="M10 2c-6 2-9 8-8 16 2 12 10 25 20 31 6 3 11 2 14-2l3-4-9-9-5 4c-4-2-9-10-10-15l5-3-4-12z" fill="#fff"/></svg></div>
      <div class="input">Enter Your Phone Number</div>
    </div>
    <div class="btn-view">View Plan
      <svg width="38" height="38" viewBox="0 0 38 38" aria-hidden="true"><circle cx="15" cy="15" r="11" fill="none" stroke="#fff" stroke-width="4"/><path d="M23 23l12 12" stroke="#fff" stroke-width="5" stroke-linecap="round"/></svg>
    </div>
  </section>

  <footer>
    <div class="footer-rule"></div>
    <p class="footer-links">HOME | ABOUT US | PLANS | EQUIPMENT | CALL RATES | SUPPORT | CONTACT US</p>
    <div class="footer-bar">
      <p class="copyright">Copyright © 2013 veltrix.example</p>
      <div class="social">
        <span role="img" aria-label="Chatterly"></span>
        <span role="img" aria-label="Plexo +"></span>
        <span role="img" aria-label="Linkora"></span>
        <span role="img" aria-label="Feedline"></span>
        <span role="img" aria-label="Chirpnet"></span>
      </div>
    </div>
  </footer>
</div>
</body>
</html>
```